RW Talbrook LLC Business Card - Civil Engineering & Consulting Firm

We need a Business Card that is elegant, and masculine.  It is our Professional Civil Engineering & Consulting Company located in San Antonio TX (Not s construction or builder firm- no gears & no tool images please). We provide civil engineering services including  commercial site plans, grading and drainage plans, utility plans, hydraulics and hydrology, land planning, utility coordination, and other general civil engineering services related to commercial and residential development.
We have 2 existing Logos. We would like to convey reliability, strength, trustworthiness and attention to detail.  Blues and orange tones as per logo We are OK with the use of a darker blue in the mix.  We have 2 logo versions - Full Company Name Logo to go on the back of card, & Small Icon Logo for the front w/ personal Info.

Target Market(s)
Architects, Real Estate Developers, Other Strctural Engineers, Surveyers, General Contractors
Industry/Entity Type
Professional Civil Engineering
Contact Information for Business Card
Name, Position, Address, Cell & Office #, email, and company website
Font styles to use
Other font styles liked:
- Avian
Requirements
Should not have
- No Tools, No Gears, no Cranes, or Construction Equipment.

```html
<!DOCTYPE html>
<html lang="en">
<head>
<meta charset="utf-8">
<title>RW Talbrook LLC – Business Card</title>
<link rel="stylesheet" href="https://fonts.googleapis.com/css2?family=Montserrat:wght@300&family=Open+Sans:ital,wght@0,400;1,400&display=swap">
<style>
  :root {
    --backdrop: #a7a8ac;
    --paper: #ffffff;
    --navy-deep: #03002e;
    --navy: #120a42;
    --sky: #7aaedb;
    --amber: #f0922e;
    --gold: #fbb614;
    --ink: #2b2b2b;
  }
  * { margin: 0; padding: 0; box-sizing: border-box; }
  html, body { width: 1200px; height: 960px; overflow: hidden; }
  body { background: var(--backdrop); position: relative; font-family: "Open Sans", sans-serif; color: var(--ink); }

  .card { position: absolute; overflow: hidden; }
  .card-front { left: 69px; top: 73px; width: 480px; height: 840px; background: var(--paper); }
  .edge-gold { position: absolute; left: 439px; top: 0; width: 15px; height: 100%; background: var(--gold); }
  .edge-navy { position: absolute; left: 454px; top: 0; width: 26px; height: 100%; background: var(--navy-deep); }

  .brand { position: absolute; left: 53px; top: 284px; width: 330px; }
  .brand-row { display: flex; align-items: center; gap: 10px; }
  .brand-square { width: 14px; height: 14px; background: var(--amber); flex: none; }
  .brand-name { font-family: "Montserrat", sans-serif; font-weight: 300; font-size: 27px; letter-spacing: 2px; color: var(--sky); white-space: nowrap; }
  .brand-rule { height: 2px; background: var(--sky); margin: 8px 0 8px 24px; width: 246px; }
  .brand-tag { font-family: "Montserrat", sans-serif; font-weight: 300; font-size: 11.5px; letter-spacing: 4.6px; color: var(--amber); margin-left: 24px; white-space: nowrap; }

  .person { position: absolute; left: 53px; top: 494px; }
  .person-name { font-style: italic; font-size: 35px; line-height: 1.1; }
  .person-role { font-size: 18px; line-height: 24px; margin-top: 8px; }

  .address { position: absolute; left: 53px; top: 594px; font-size: 18px; line-height: 24px; }

  .contacts { position: absolute; left: 53px; list-style: none; font-size: 18px; }
  .contacts li { display: flex; align-items: center; height: 30px; }
  .contacts svg { width: 20px; height: 20px; margin-right: 19px; fill: var(--ink); flex: none; }
  .contacts-phone { top: 663px; }
  .contacts-web { top: 741px; }

  .card-back { left: 601px; top: 75px; width: 481px; height: 840px; background: linear-gradient(90deg, var(--navy-deep), var(--navy)); display: flex; align-items: center; justify-content: center; }
  .back-mark { display: flex; align-items: center; gap: 12px; }
  .back-square { width: 18px; height: 18px; background: var(--amber); }
  .back-name { font-family: "Montserrat", sans-serif; font-weight: 300; font-size: 30px; letter-spacing: 3px; color: var(--sky); }
</style>
</head>
<body>
  <section class="card card-front">
    <div class="brand">
      <div class="brand-row">
        <span class="brand-square"></span>
        <span class="brand-name">RW TALBROOK LLC</span>
      </div>
      <div class="brand-rule"></div>
      <div class="brand-tag">CONSULTING ENGINEERS</div>
    </div>

    <div class="person">
      <div class="person-name">Name Title</div>
      <div class="person-role">designation</div>
    </div>

    <div class="address">suit # 00, Lorem ipsum<br>Lorem Lorem ipsum</div>

    <ul class="contacts contacts-phone">
      <li><svg viewBox="0 0 20 20" aria-hidden="true"><rect x="1" y="1" width="18" height="18" rx="3"/><path d="M7 4c-1 1-2 3 0 7s4 5 6 5l1-2-2-2-1 1c-1-1-2-2-3-4l1-1-1-3z" fill="#fff"/></svg>000-000-0000</li>
      <li><svg viewBox="0 0 20 20" aria-hidden="true"><rect x="5" y="1" width="10" height="8"/><rect x="2" y="9" width="16" height="6"/><rect x="1" y="16" width="18" height="3"/></svg>000-000-0000</li>
    </ul>

    <ul class="contacts contacts-web">
      <li><svg viewBox="0 0 20 20" aria-hidden="true"><path d="M1 8l9-6 9 6v10H1z"/><path d="M3 8l7 5 7-5" fill="none" stroke="#fff" stroke-width="1.5"/></svg>abcd@TalbrookCE.com</li>
      <li><svg viewBox="0 0 20 20" aria-hidden="true"><path d="M7 1h2v9l1-2h2v1l1-1h2v1l1-1h2v6l-2 5H8l-4-6 1-1 2 2z"/></svg>www.TalbrookCE.com</li>
    </ul>

    <div class="edge-gold"></div>
    <div class="edge-navy"></div>
  </section>

  <section class="card card-back">
    <div class="back-mark">
      <span class="back-square"></span>
      <span class="back-name">RW TALBROOK LLC</span>
    </div>
  </section>
</body>
</html>
```